Harbrook Techlink Solutions

We need a Logo and Website for our company based in London. We are a IT recruitment company . We provide quality resources to top IT company across UK.

Industry/Entity Type

It Company

Number of Pages Required

4 page

```html
<!DOCTYPE html>
<html lang="en">
<head>
<meta charset="utf-8">
<title>Harbrook Techlink Solutions – IT Recruitment</title>
<link rel="stylesheet" href="https://fonts.googleapis.com/css2?family=Roboto+Condensed:wght@400;500;700&family=Open+Sans:wght@400;600&display=swap">
<style>
  :root{
    --page:#e8e8e8;
    --bar-dark:rgba(8,55,85,.82);
    --nav-blue:#1ab1ea;
    --nav-active:#0b4a6c;
    --accent:#2aaee6;
    --panel:rgba(10,55,82,.72);
    --form-blue:#1aa3dc;
    --label:#0b3550;
    --orange:#ff6a00;
    --black:#050505;
    --button-dark:#063a55;
    --footer:#00455f;
    --footer-head:#2aaee6;
    --white:#ffffff;
    --cond:"Roboto Condensed", "Arial Narrow", sans-serif;
    --body:"Open Sans", Arial, sans-serif;
  }
  *{box-sizing:border-box;margin:0;padding:0}
  html,body{width:1200px;height:1150px;overflow:hidden}
  body{background:var(--page);position:relative;font-family:var(--body);color:var(--white)}
  .site{position:absolute;left:15px;top:15px;width:1170px;height:1120px;background:var(--white)}
  .hero-photo{position:absolute;left:0;top:0;width:1170px;height:800px;
    background:
      radial-gradient(ellipse 420px 260px at 240px 250px,#cfdce6 0%,rgba(207,220,230,0) 70%),
      radial-gradient(ellipse 380px 240px at 900px 230px,#b9cad8 0%,rgba(185,202,216,0) 70%),
      radial-gradient(ellipse 500px 200px at 330px 700px,#e6eef4 0%,rgba(230,238,244,0) 75%),
      linear-gradient(180deg,#5b7d97 0%,#3d5f7c 35%,#1f3c57 60%,#86a3ba 85%,#c7d6e1 100%);}
  .top-bar{position:absolute;left:0;top:20px;width:1170px;height:48px;background:var(--bar-dark)}
  .site-search{position:absolute;left:599px;top:11px;width:190px;height:26px;background:var(--white);
    border-radius:4px;border:1px solid #9bb;font:700 11px var(--body);color:#1a2a35;padding:6px 0 0 10px;letter-spacing:-.2px}
  .site-search svg{position:absolute;right:8px;top:3px}
  .phone{position:absolute;left:846px;top:13px;height:22px;display:flex;align-items:center;gap:8px;
    font:600 15px var(--body);color:var(--white)}
  .social{position:absolute;left:1072px;top:14px;display:flex;gap:9px}
  .social span{width:18px;height:18px;border-radius:50%;background:var(--white)}
  .nav-bar{position:absolute;left:0;top:68px;width:1170px;height:48px;background:var(--nav-blue)}
  .brand{position:absolute;left:64px;top:6px;font:500 29px/36px var(--cond);color:var(--white);letter-spacing:.2px}
  .main-nav{position:absolute;right:26px;top:16px;display:flex;gap:14px;list-style:none;
    font:700 14.5px var(--cond);color:var(--white)}
  .main-nav .active{color:var(--nav-active);position:relative}
  .main-nav .active::after{content:"";position:absolute;left:50%;margin-left:-7px;top:25px;
    border:7px solid transparent;border-bottom-color:var(--nav-active);border-top:0}
  .finder{position:absolute;left:50px;top:310px;width:1071px;height:321px;background:var(--panel);
    border:2px solid var(--white);border-radius:3px}
  .finder-badge{position:absolute;left:25px;top:285px;width:76px;height:76px}
  .finder-title{position:absolute;left:73px;top:21px;font:500 30px var(--cond);color:var(--white);letter-spacing:-.2px}
  .finder-title em{font-style:normal;color:var(--accent)}
  .view-all{position:absolute;left:783px;top:21px;width:254px;height:35px;background:var(--black);
    border-radius:3px;display:flex;align-items:center;gap:12px;padding-left:44px;
    font:700 15px var(--cond);color:var(--white)}
  .search-form{position:absolute;left:13px;top:78px;width:1041px;height:226px;background:var(--form-blue);
    border:2px solid var(--white);border-radius:4px}
  .role-tabs{position:absolute;left:8px;top:8px;width:1021px;height:40px}
  .role-tabs text{font:500 17px var(--cond);fill:var(--white)}
  .field-label{position:absolute;font:500 15px var(--cond);color:var(--label)}
  .field{position:absolute;height:40px;background:var(--white);border-radius:2px;
    font:500 14.5px var(--cond);color:#1c2630;padding:11px 0 0 13px}
  .field.select::after{content:"";position:absolute;right:10px;top:17px;border:8px solid transparent;
    border-top:7px solid #333;border-bottom:0}
  .search-btn{position:absolute;left:769px;top:158px;width:260px;height:40px;background:var(--button-dark);
    border-radius:3px;display:flex;align-items:center;justify-content:center;gap:10px;
    font:700 16px var(--cond);color:var(--white)}
  .footer{position:absolute;left:0;top:800px;width:1170px;height:290px;background:var(--footer)}
  .footer h3{font:700 14px var(--body);color:var(--footer-head);margin-bottom:11px;letter-spacing:-.1px}
  .footer p{font:400 12.4px/19.2px var(--body);width:340px}
  .footer ul{list-style:none;font:400 12.4px/21px var(--body)}
  .footer-col{position:absolute;top:34px}
  .legal{top:61px}
  .copyright{position:absolute;left:0;top:1090px;width:1170px;height:30px;background:var(--white);
    text-align:center;font:400 9px/30px var(--body);color:#555}
</style>
</head>
<body>
<div class="site">
  <div class="hero-photo" role="img" aria-label="Photo of smiling young professionals talking around a meeting table"></div>

  <header>
    <div class="top-bar">
      <div class="site-search">SEARCH SITE
        <svg width="20" height="20" viewBox="0 0 20 20" fill="none" stroke="#888" stroke-width="2"><circle cx="8" cy="8" r="6"/><path d="M12.5 12.5l5 5"/></svg>
      </div>
      <div class="phone">
        <svg width="22" height="22" viewBox="0 0 22 22" fill="none" stroke="#fff" stroke-width="1.6"><circle cx="11" cy="11" r="9.5"/><path d="M7.5 6.5c-.8.8-.6 2.6 1.5 5s4.3 3.1 5.2 2.3l1-1-2-2-1 .8c-.6-.3-2.1-1.7-2.5-2.5l.8-1-2-2z" fill="#fff" stroke="none"/></svg>
        1-800-555-019-2468
      </div>
      <div class="social" aria-label="Social links"><span></span><span></span><span></span></div>
    </div>
    <div class="nav-bar">
      <div class="brand">Harbrook Techlink Solutions</div>
      <ul class="main-nav">
        <li class="active">HOME</li><li>JOB SEEKERS</li><li>EMPLOYERS</li><li>ABOUT US</li><li>SERVICES</li><li>NEWS</li><li>CONTACT</li>
      </ul>
    </div>
  </header>

  <section class="finder">
    <h1 class="finder-title">FIND YOUR <em>LOCAL &amp; SPECIALIST IT AGENCIES</em></h1>
    <div class="view-all">
      <svg width="36" height="20" viewBox="0 0 36 20" fill="#fff"><rect x="0" y="0" width="6" height="4"/><rect x="9" y="0" width="27" height="4"/><rect x="0" y="8" width="6" height="4"/><rect x="9" y="8" width="27" height="4"/><rect x="0" y="16" width="6" height="4"/><rect x="9" y="16" width="27" height="4"/></svg>
      VIEW ALL LISTINGS
    </div>
    <form class="search-form">
      <svg class="role-tabs" viewBox="0 0 1021 40" width="1021" height="40">
        <rect width="1021" height="40" fill="#050505"/>
        <polygon points="112,0 142,0 122,40 92,40" fill="#1aa3dc"/>
        <polygon points="142,0 352,0 332,40 122,40" fill="#ff6a00"/>
        <polygon points="352,0 362,0 342,40 332,40" fill="#1aa3dc"/>
        <polygon points="549,0 559,0 539,40 529,40" fill="#1aa3dc"/>
        <text x="47" y="27">I AM</text>
        <text x="186" y="27">A CANDIDATE</text>
        <text x="389" y="27">AN EMPLOYER</text>
      </svg>
      <svg style="position:absolute;left:230px;top:46px" width="16" height="8"><polygon points="0,0 16,0 8,8" fill="#ff6a00"/></svg>

      <label class="field-label" style="left:11px;top:57px">INDUSTRY</label>
      <div class="field select" style="left:8px;top:78px;width:360px">INFORMATION TECHNOLOGY</div>
      <label class="field-label" style="left:391px;top:57px">INDUSTRY SUB SECTOR</label>
      <div class="field select" style="left:388px;top:78px;width:360px">PLEASE CHOOSE ONE</div>
      <label class="field-label" style="left:770px;top:57px">JOB TYPE</label>
      <div class="field select" style="left:768px;top:78px;width:260px">ALL</div>

      <label class="field-label" style="left:11px;top:137px">LOCATION</label>
      <div class="field" style="left:8px;top:158px;width:360px">POSTCODE, TOWN OR COUNTY</div>
      <label class="field-label" style="left:391px;top:137px">ORDER RESULTS BY</label>
      <div class="field" style="left:388px;top:158px;width:360px">PLEASE CHOOSE ONE</div>
      <div class="search-btn">
        <svg width="26" height="26" viewBox="0 0 26 26" fill="none" stroke="#fff" stroke-width="2.6"><circle cx="15" cy="11" r="8"/><path d="M9 17l-6 6"/></svg>
        SEARCH
      </div>
    </form>
  </section>
  <svg class="finder-badge" viewBox="0 0 76 76">
    <circle cx="38" cy="38" r="37" fill="#0a4a66"/>
    <circle cx="34" cy="33" r="17" fill="none" stroke="#fff" stroke-width="6"/>
    <path d="M46 45l15 15" stroke="#fff" stroke-width="9" stroke-linecap="round"/>
  </svg>

  <footer class="footer">
    <div class="footer-col" style="left:73px">
      <h3>About Harbrook Techlink Solutions</h3>
      <p>Lorem ipsum dolor sit amet, consectetuer adipiscing elit, sed diam nonummy nibh euismod tincidunt ut laoreet dolore magna aliquam erat volutpat. Ut wisi enim ad minim veniam, quis nostrud exerci tation ullamcorper suscipit lobortis nisl ut aliquip ex ea commodo consequat. Duis autem vel eum iriure dolor in hendrerit in vulputate velit esse molestie consequat, vel illum dolore eu feugiat nulla facilisis at vero eros et accumsan et iusto odio dignissim qui blandit praesent luptatum zzril delenit augue duis dolore te feugait nulla facilisi.</p>
    </div>
    <div class="footer-col" style="left:484px">
      <h3>Our Corporate</h3>
      <ul><li>Company</li><li>Press Room</li><li>Fast Facts</li><li>Careers</li><li>Contact</li></ul>
    </div>
    <div class="footer-col" style="left:661px">
      <h3>Job Seekers</h3>
      <ul><li>Browse IT Jobs</li><li>Submit Resume</li><li>Benefits</li><li>Career Resources</li><li>Testimonials</li></ul>
    </div>
    <div class="footer-col" style="left:839px">
      <h3>Employers</h3>
      <ul><li>Industry Expertise</li><li>Testimonials</li><li>Q &amp; A</li><li>Salary Guide</li></ul>
    </div>
    <div class="footer-col legal" style="left:1021px">
      <ul><li>Terms of Use</li><li>Copyright</li><li>Privacy Policy</li></ul>
    </div>
  </footer>
  <div class="copyright">COPYRIGHT © 2016 HARBROOK TECHLINK SOLUTIONS. ALL RIGHTS RESERVED.</div>
</div>
</body>
</html>
```